Business Stationery Design

I would like to get some stationery designed for my company. The stationery should include a letterhead, envelope, and business card. We are a technology consulting company specializing in Healthcare IT, and Education management systems. The colors of the stationery should match the logo. The logo is uploaded.

Target Market(s)

Hospitals, Clinics. Doctors offices. Private Schools.

Industry/Entity Type

Business

```html
<!DOCTYPE html>
<html lang="en">
<head>
<meta charset="utf-8">
<title>Oakmere Advisory Group – Business Card</title>
<link href="https://fonts.googleapis.com/css2?family=Roboto:wght@400;500&display=swap" rel="stylesheet">
<style>
  :root {
    --backdrop: #2b2b2b;
    --green: #76bc2c;
    --yellow: #f6bb00;
    --paper: #f2f2f2;
    --ink: #555555;
    --rule: #a8a8a8;
    --white: #ffffff;
  }
  * { margin: 0; padding: 0; box-sizing: border-box; }
  html, body { width: 1200px; height: 960px; overflow: hidden; }
  body {
    background: var(--backdrop);
    font-family: "Roboto", Arial, sans-serif;
    position: relative;
  }
  .card {
    position: absolute;
    border-radius: 18px;
    overflow: hidden;
  }
  .card-front { left: 320px; top: 100px; width: 598px; height: 355px; }
  .card-front .front-art { position: absolute; inset: 0; }
  .front-brand {
    position: absolute; right: 28px; top: 238px;
    color: var(--white); text-align: right; font-weight: 400;
  }
  .front-brand .brand-name { font-size: 42px; line-height: 1; display: block; }
  .front-brand .brand-sub { font-size: 15px; line-height: 1.2; display: block; }
  .front-web {
    position: absolute; right: 28px; top: 310px;
    color: var(--white); font-size: 14px; letter-spacing: 3px;
  }

  .card-back {
    left: 320px; top: 493px; width: 600px; height: 340px;
    background: var(--paper);
  }
  .back-brand {
    position: absolute; right: 34px; top: 36px;
    text-align: right; color: var(--green); font-weight: 400;
  }
  .back-brand .brand-dot {
    display: block; width: 46px; height: 46px; border-radius: 50%;
    background: var(--yellow); margin: 0 18px 14px auto;
  }
  .back-brand .brand-name { display: block; font-size: 27px; line-height: 1; }
  .back-brand .brand-sub { display: block; font-size: 10px; line-height: 1.3; }

  .holder { position: absolute; left: 36px; top: 172px; }
  .holder-name { color: var(--green); font-size: 20px; font-weight: 500; line-height: 1.2; }
  .holder-title { color: var(--yellow); font-size: 14px; font-weight: 500; margin-top: 2px; }
  .divider {
    position: absolute; left: 38px; right: 38px; top: 226px;
    border-top: 1px solid var(--rule);
  }
  .contact-list {
    position: absolute; left: 36px; top: 240px; list-style: none;
    color: var(--ink); font-size: 14px;
  }
  .contact-list li { display: flex; align-items: center; height: 19px; }
  .contact-list svg { width: 13px; height: 13px; margin-right: 10px; fill: var(--green); }
  .address {
    position: absolute; right: 34px; top: 258px; text-align: right;
    color: var(--ink); font-size: 14px; line-height: 19px; font-style: normal;
  }
</style>
</head>
<body>

<section class="card card-front">
  <svg class="front-art" viewBox="0 0 598 355" aria-hidden="true">
    <rect width="598" height="355" fill="var(--yellow)"/>
    <circle cx="222" cy="240" r="225" fill="var(--green)"/>
    <rect x="222" y="0" width="376" height="355" fill="var(--green)"/>
    <path d="M 32 365 A 225 225 0 1 1 436 175" fill="none" stroke="var(--white)" stroke-width="9"/>
  </svg>
  <div class="front-brand">
    <span class="brand-name">Oakmere</span>
    <span class="brand-sub">Advisory Group</span>
  </div>
  <div class="front-web">www.oakmereadvisory.com</div>
</section>

<section class="card card-back">
  <div class="back-brand">
    <span class="brand-dot"></span>
    <span class="brand-name">Oakmere</span>
    <span class="brand-sub">Advisory Group</span>
  </div>

  <div class="holder">
    <div class="holder-name">DANIEL REYES</div>
    <div class="holder-title">CEO/FOUNDER</div>
  </div>
  <div class="divider"></div>

  <ul class="contact-list">
    <li><svg viewBox="0 0 24 24"><path d="M6.6 10.8a15.2 15.2 0 0 0 6.6 6.6l2.2-2.2c.3-.3.7-.4 1-.2 1.1.4 2.3.6 3.6.6.6 0 1 .4 1 1V20c0 .6-.4 1-1 1A17 17 0 0 1 3 4c0-.6.4-1 1-1h3.5c.6 0 1 .4 1 1 0 1.3.2 2.5.6 3.6.1.3 0 .7-.2 1z"/></svg>555 214 0137</li>
    <li><svg viewBox="0 0 24 24"><path d="M7 1h10a2 2 0 0 1 2 2v18a2 2 0 0 1-2 2H7a2 2 0 0 1-2-2V3a2 2 0 0 1 2-2zm0 3v14h10V4z"/></svg>555 382 7416</li>
    <li><svg viewBox="0 0 24 24"><path d="M6 2h12v5H6zM3 8h18a1 1 0 0 1 1 1v8h-4v5H6v-5H2V9a1 1 0 0 1 1-1zm5 7v5h8v-5z"/></svg>555 609 2285</li>
    <li><svg viewBox="0 0 24 24"><path d="M2 5h20v14H2zm2 2v.5l8 5 8-5V7z"/></svg>daniel@oakmereadvisory.com</li>
  </ul>

  <address class="address">
    214 Alder Court<br>
    Juneau, Alaska 99801<br>
    www.oakmereadvisory.com
  </address>
</section>

</body>
</html>
```